Stabilization Flyer

We are looking for a single document that outlines the info below - we want to emphasize that we can help child cares in the process and then we can help them make any award money go further through our program -
Don’t leave money on the table – as a child care owner you have access to grant money, but time is running out.

President Halvorsen signed the National Renewal Fund Act of 2021 (NRF). This plan includes $24 billion in child care stabilization grant funding. These funds will help keep early childhood educators and family child care providers keep their doors open and provide a critical step to paving the way for a strong economic recovery and a more equitable future.

Each State has its own application process – most licensed child care centers are eligible for grants with awards up to $400,000 per program. Awarded dollars is based upon your center’s capacity.

Grants are good for the following categories

Child care providers can use stabilization subgrants to cover these expenses:
• Wages and benefits, including increases in compensation for any staff.
• Rent, utilities, facilities maintenance and minor renovations, and insurance.
• Personal protective equipment, cleaning supplies, and other health and safety measures.
• Equipment and supplies used to respond to COVID-19.
• Material goods (i.e., to facilitate play or safe sleep) or services (i.e., food) used for the operation of the program. Yes, Food is an allowable expense.
• Mental health services for children and employees

If you have not applied for the grant, we can help point you in the right direction. Just email stablization@pantryandgoodsdepot.com or call 877. 391.6052 and we will send you the links on how to file within your State. No purchase is necessary for this guidance, but we would love the opportunity to show you how we can stretch your purchases by up to 30%.

Target Market(s)

child care centers

Industry/Entity Type

child care is the target

Requirements
Must have
• website www.pantryandgoodsdepot.com
Nice to have
• we have a video that could be embedded https://www.pantryandgoodsdepot.com/video-resources/

```html
<!DOCTYPE html>
<html lang="en">
<head>
<meta charset="utf-8">
<title>Stabilization Grant Flyer</title>
<link rel="stylesheet" href="https://fonts.googleapis.com/css2?family=Baloo+2:wght@700;800&family=Open+Sans:wght@400;600;700&display=swap">
<style>
  :root {
    --green: #6dbb63;
    --green-light: #a9da98;
    --green-pale: #e3f2dc;
    --blue-text: #2f7ad0;
    --navy: #1f4f93;
    --lavender: #dde3f5;
    --ink: #222;
    --grey-bg: #444446;
    --white: #fff;
  }
  * { margin: 0; padding: 0; box-sizing: border-box; }
  html, body { width: 720px; height: 1200px; overflow: hidden; background: var(--grey-bg); }
  body { font-family: "Open Sans", sans-serif; color: var(--ink); }
  .flyer {
    position: absolute; left: 0; top: 134px; width: 720px; height: 932px;
    background: var(--white); overflow: hidden;
  }
  .backdrop { position: absolute; inset: 0; }
  .brand { position: absolute; left: 43px; top: 46px; display: flex; align-items: center; gap: 10px; }
  .brand-mark { width: 26px; height: 26px; background: var(--blue-text); }
  .brand-name { font-weight: 400; font-size: 26px; line-height: 1; color: #555; letter-spacing: -0.4px; }
  .brand-tagline { position: absolute; left: 80px; top: 85px; font-size: 10px; font-weight: 600; color: var(--blue-text); }
  .headline { position: absolute; left: 78px; top: 110px; font-family: "Baloo 2", sans-serif; font-weight: 800; line-height: 1; }
  .headline .line-small { display: block; font-size: 38px; line-height: 46px; color: var(--blue-text); }
  .headline .line-big { display: block; font-size: 64px; line-height: 54px; color: var(--green); padding-top: 6px; margin-left: 35px; }
  .subhead { position: absolute; left: 43px; top: 252px; font-size: 18.5px; font-weight: 700; color: var(--green); line-height: 26px; }
  .intro { position: absolute; left: 43px; top: 315px; width: 400px; font-size: 11px; line-height: 16px; letter-spacing: -0.1px; }
  .eligibility { position: absolute; left: 43px; top: 406px; width: 410px; font-size: 11px; line-height: 16px; letter-spacing: -0.1px; color: var(--blue-text); font-weight: 600; }
  .photo, .illustration { position: absolute; border-radius: 50%; }
  .photo { left: 449px; top: -21px; width: 268px; height: 268px; background: radial-gradient(circle at 45% 45%, #e7c2a6, #7e9a58 60%, #4c6e3a); }
  .illustration { left: 449px; top: 204px; width: 268px; height: 268px; background: radial-gradient(circle at 50% 50%, #f0c98a 0 30%, #6dbb63 55%); }
  .banner {
    position: absolute; left: 43px; top: 475px; width: 637px; height: 47px; border-radius: 12px;
    background: linear-gradient(#d9efcf, #9fd58f); box-shadow: 0 2px 4px rgba(0,0,0,.25);
    font-family: "Baloo 2", sans-serif; font-weight: 800; font-size: 25px; color: #333;
    display: flex; align-items: center; justify-content: center;
  }
  .expenses-title { position: absolute; left: 0; width: 720px; top: 540px; text-align: center; color: var(--white); font-family: "Baloo 2", sans-serif; font-weight: 800; font-size: 20.5px; line-height: 25px; }
  .expense-list { position: absolute; top: 597px; list-style: none; color: var(--white); font-size: 13.4px; line-height: 19px; }
  .expense-list li { position: relative; margin-bottom: 9px; }
  .expense-list li::before {
    content: "✓"; position: absolute; left: 0; top: 3px; width: 13px; height: 13px; border-radius: 50%;
    background: var(--green); color: var(--white); font-size: 9px; line-height: 13px; text-align: center; font-weight: 700;
  }
  .expense-list.left { left: 48px; width: 295px; }
  .expense-list.left li { padding-left: 27px; }
  .expense-list.right { left: 377px; width: 292px; }
  .expense-list.right li { padding-left: 18px; }
  .column-rule { position: absolute; left: 357px; top: 600px; width: 2px; height: 158px; background: var(--green); }
  .contact { position: absolute; left: 23px; top: 786px; width: 677px; height: 108px; background: var(--green); border-radius: 14px 14px 0 0; }
  .contact-lead {
    position: absolute; left: 20px; top: -12px; width: 637px; height: 32px; background: var(--navy); border-radius: 8px;
    color: var(--white); font-size: 12px; font-weight: 700; text-align: center; line-height: 32px; letter-spacing: -0.2px;
  }
  .contact-line { position: absolute; left: 0; width: 100%; top: 32px; text-align: center; font-size: 18px; line-height: 26px; font-weight: 700; color: #1f1f1f; }
  .contact-line .dot { display: inline-block; width: 16px; height: 16px; border-radius: 50%; background: var(--blue-text); vertical-align: -2px; margin-right: 5px; }
  .contact-note { position: absolute; left: 30px; width: 617px; top: 62px; text-align: center; font-size: 10.6px; line-height: 15px; color: #1f1f1f; }
  .footer { position: absolute; left: 0; top: 894px; width: 720px; height: 38px; background: var(--white); display: flex; align-items: center; justify-content: center; gap: 22px; font-size: 12px; font-weight: 700; }
  .footer .rule { width: 2px; height: 24px; background: var(--green); }
</style>
</head>
<body>
<main class="flyer">
  <svg class="backdrop" width="720" height="932" viewBox="0 0 720 932">
    <defs>
      <linearGradient id="blueFade" x1="0" y1="0" x2="0" y2="1">
        <stop offset="0" stop-color="#3a80cf"/>
        <stop offset="1" stop-color="#2a62ab"/>
      </linearGradient>
    </defs>
    <path d="M0 462 C 180 446, 430 428, 720 440 L720 932 L0 932 Z" fill="#8cc97d"/>
    <path d="M0 480 C 200 478, 450 462, 720 462 L720 932 L0 932 Z" fill="url(#blueFade)"/>
    <path d="M0 105 A 62 62 0 0 1 0 229 Z" fill="#dde3f5"/>
    <circle cx="0" cy="172" r="52" fill="#6dbb63"/>
    <path d="M440 200 A 140 140 0 0 1 585 -25 L 600 -25 A 120 120 0 0 0 460 200 Z" fill="#6dbb63"/>
    <path d="M500 20 A 150 150 0 0 1 720 0 L720 20 A 140 140 0 0 0 505 30 Z" fill="#e3f2dc"/>
  </svg>

  <div class="brand"><span class="brand-mark"></span><span class="brand-name">Greenleaf Provisions</span></div>
  <div class="brand-tagline">Stretch Every Dollar</div>

  <h1 class="headline">
    <span class="line-small">Don’t Leave</span>
    <span class="line-big">Money</span>
    <span class="line-small">On The Table –</span>
  </h1>

  <p class="subhead">as a child care owner you have access<br>to grant money, but time is running out.</p>

  <p class="intro">President Halvorsen signed the National Renewal Fund Act of 2021 (NRF). This plan includes $24 billion in child care stabilization grant funding. These funds will help keep early childhood educators and family child care providers keep their doors open and provide a critical step to paving the way for a strong economic recovery and a more equitable future.</p>

  <p class="eligibility">Each State has its own application process – most licensed child care centers are eligible for grants with awards up to $400,000 per program. Awarded dollars is based upon your center’s capacity.</p>

  <div class="illustration" role="img" aria-label="Illustration of a money bag with a dollar sign, gold coins and banknotes"></div>
  <div class="photo" role="img" aria-label="Photo of three smiling young children outdoors"></div>

  <h2 class="banner">Grants are good for the following categories</h2>

  <h3 class="expenses-title">Child care providers can use stabilization subgrants<br>to cover these expenses:</h3>

  <ul class="expense-list left">
    <li>Wages and benefits, including increases in compensation for any staff.</li>
    <li>Rent, utilities, facilities maintenance and minor renovations, and insurance.</li>
    <li>Personal protective equipment, cleaning supplies, and other health and safety measures.</li>
  </ul>
  <div class="column-rule"></div>
  <ul class="expense-list right">
    <li>Equipment and supplies used to respond to COVID-19.</li>
    <li>Material goods (i.e., to facilitate play or safe sleep) or services (i.e., food) usedfor the operation of the program. Yes, Food is an allowable expense.</li>
    <li>Mental health services for children and employees</li>
  </ul>

  <section class="contact">
    <p class="contact-lead">If you have not applied for the grant, we can help point you in the right direction. Just email</p>
    <p class="contact-line"><span class="dot"></span>stablization@pantryandgoodsdepot.com or call <span class="dot"></span>877. 391.6052</p>
    <p class="contact-note">and we will send you the links on how to file within your State. No purchase is necessary for this guidance, but we would love the opportunity to show you how we can stretch your purchases by up to 30%.</p>
  </section>

  <footer class="footer">
    <span>https://www.pantryandgoodsdepot.com/video-resources/</span>
    <span class="rule"></span>
    <span>www.pantryandgoodsdepot.com</span>
  </footer>
</main>
</body>
</html>
```